Postcard design to acquire new clients for my Property Management Company

I'm looking for a postcard design that I can send to prospective clients detailing information about my company and services.
Postcard should be eye catching and contain information from www.brightkeyrentals-example.com. I've provided a few screen shots for the most important information and my logo.
Target Market(s)
Real Estate
Industry/Entity Type
Real Estate
Font styles to use
Sans Serif
Requirements
Must have
- Must be eye catching!! this will be a direct mail piece - I'd like for the card to be read and not tossed in the trash immediately.
Design que from the logo.
A place to write / print the receipts name and address.
our physical address - 2287 Marble Lane, Lubbock, TX 79555.
Should not have
- the contact information on the business card is not accurate - please use info from website.

```html
<!DOCTYPE html>
<html lang="en">
<head>
<meta charset="utf-8">
<title>BrightKey Rentals – Direct Mail Postcard</title>
<link href="https://fonts.googleapis.com/css2?family=Montserrat:wght@300;400;500;600;700;800&display=swap" rel="stylesheet">
<style>
  :root{
    --navy:#0b4a86;
    --navy-dark:#08457f;
    --grey:#9b9b9b;
    --grey-light:#cfcfcf;
    --backdrop:#7d8289;
    --white:#ffffff;
    --ink:#333333;
  }
  *{margin:0;padding:0;box-sizing:border-box}
  html,body{width:856px;height:1200px;overflow:hidden;background:var(--backdrop);font-family:"Montserrat",sans-serif}
  .card{position:absolute;left:100px;width:655px;height:473px;background:var(--white);overflow:hidden}
  .card--front{top:110px}
  .card--back{top:644px}
  .abs{position:absolute}

  /* brand name */
  .brand{position:absolute;color:var(--navy);font-weight:600;letter-spacing:.22em;line-height:1.15;text-transform:uppercase}
  .card--front .brand{left:22px;top:24px;font-size:17px}
  .card--back .brand{left:411px;top:16px;font-size:24px}

  /* front */
  .headline{position:absolute;left:22px;top:88px;z-index:3;color:var(--navy);font-weight:800;font-size:42px;line-height:46px;letter-spacing:-.01em}
  .headline .on-photo{color:var(--white)}
  .photo{position:absolute;left:251px;top:0;width:404px;height:287px;background:linear-gradient(135deg,#4f4c46 0%,#6b6458 35%,#b07a3f 55%,#d8d3c8 70%,#4a4a4c 100%)}
  .frames{position:absolute;left:0;top:0;z-index:2}
  .tagline{position:absolute;left:22px;top:324px;color:var(--grey);font-weight:700;font-size:14.2px;line-height:17px;letter-spacing:.02em}

  .plan{position:absolute;top:327px;text-align:center}
  .plan__name{position:relative;display:block;height:17px;margin:0 4px;color:var(--white);font-weight:300;font-size:14.5px;line-height:17px}
  .plan__name::before{content:"";position:absolute;inset:0;background:var(--grey);transform:skewX(-32deg);border-left:3px solid var(--navy);border-right:3px solid var(--navy);box-shadow:-5px 0 0 -2px var(--white),5px 0 0 -2px var(--white);z-index:-1}
  .plan__note{display:block;margin-top:1px;font-size:8px;color:var(--ink)}
  .plan__rate{display:block;margin-top:-1px;font-size:30px;font-weight:800;color:var(--navy);line-height:32px}
  .plan__basis{display:block;font-size:9px;color:var(--ink)}

  /* bottom contact band (shared) */
  .band{position:absolute;left:0;top:0}
  .cta{position:absolute;left:23px;top:419px;width:282px;height:37px}
  .cta__text{position:absolute;left:8px;top:3px;color:var(--navy);font-weight:700;font-size:25px;white-space:nowrap}
  .contact{position:absolute;right:23px;top:405px;text-align:right;color:var(--white);font-weight:600}
  .contact__line{display:flex;justify-content:flex-end;align-items:center;gap:6px;white-space:nowrap}
  .contact__phone{font-size:20px;line-height:26px}
  .contact__mail,.contact__addr{font-size:12.5px;line-height:18px}

  /* back */
  .services-title{position:absolute;left:23px;top:28px;font-weight:800;font-size:27px;letter-spacing:.2em;color:var(--white)}
  .services-title .muted{color:var(--grey)}
  .services-sub{position:absolute;left:23px;top:55px;font-size:9px;color:var(--white);letter-spacing:.01em}
  .service{position:absolute;width:175px;height:80px}
  .service__title{position:absolute;left:19px;top:0;color:var(--navy);font-weight:700;font-size:9.6px;white-space:nowrap}
  .service__mark{position:absolute;left:0;top:1px;width:14px;height:10px}
  .service__icon{position:absolute;left:8px;top:22px;width:40px;height:40px}
  .service__body{position:absolute;left:60px;top:12px;font-size:7.4px;line-height:10.6px;color:var(--ink);white-space:nowrap}
  .divider{position:absolute;left:382px;top:81px;width:9px;height:309px;background:var(--grey)}
  .divider-end{position:absolute;left:382px;top:392px;width:9px;height:6px;background:var(--navy)}
  .stamp{position:absolute;left:560px;top:147px;width:74px;height:58px;border:1px solid #555}
  .address-line{position:absolute;left:414px;width:218px;height:0;border-top:1px solid #444}
</style>
</head>
<body>

<!-- FRONT -->
<section class="card card--front" aria-label="Postcard front">
  <div class="brand">BrightKey<br>Rentals</div>

  <div class="photo" role="img" aria-label="Photo: team of property managers reviewing plans around a conference table, seen from above"></div>
  <svg class="frames" width="655" height="473" aria-hidden="true">
    <polygon points="281,28 654,1 654,228 301,283" fill="none" stroke="var(--navy)" stroke-width="7"/>
    <polygon points="259,46 420,0 446,271 348,312" fill="none" stroke="#a3a3a3" stroke-width="6"/>
  </svg>

  <h1 class="headline">CHOOSE<br>THE RIGHT<br>PROPERTY<br>MANAGEM<span class="on-photo">ENT</span><br>SYSTEM</h1>

  <p class="tagline">SELECTING<br>THE WRONG MANAGER<br>COULD BE YOUR<br>COSTLIEST MISTAKE EVER.</p>

  <div class="plan" style="left:253px;width:111px">
    <span class="plan__name">Lease Only</span>
    <span class="plan__note">- You Just Need Tenants -</span>
    <span class="plan__rate">9%</span>
    <span class="plan__basis">of annual lease</span>
  </div>
  <div class="plan" style="left:366px;width:111px">
    <span class="plan__name">Full Service</span>
    <span class="plan__note">- Our Most Popular -</span>
    <span class="plan__rate">10%</span>
    <span class="plan__basis">of monthly rent</span>
  </div>
  <div class="plan" style="left:481px;width:148px">
    <span class="plan__name">Premium Service</span>
    <span class="plan__note">- Our Premier Service -</span>
    <span class="plan__rate">12%</span>
    <span class="plan__basis">of monthly rent</span>
  </div>

  <svg class="band" width="655" height="473" aria-hidden="true">
    <polygon points="261,400 655,400 655,473 0,473 0,460 316,460" fill="var(--navy)"/>
    <polygon points="23,419 269,419 304,456 23,456" fill="var(--grey-light)"/>
  </svg>
  <div class="cta"><span class="cta__text">Contact Our Team</span></div>
  <div class="contact">
    <div class="contact__line contact__phone">
      <svg width="13" height="13" viewBox="0 0 24 24" aria-hidden="true"><path d="M6.6 10.8a15 15 0 0 0 6.6 6.6l2.2-2.2c.3-.3.7-.4 1-.2 1.1.4 2.3.6 3.6.6.6 0 1 .4 1 1V20c0 .6-.4 1-1 1A17 17 0 0 1 3 4c0-.6.4-1 1-1h3.5c.6 0 1 .4 1 1 0 1.3.2 2.5.6 3.6.1.3 0 .7-.2 1z" fill="none" stroke="#fff" stroke-width="2"/></svg>
      (806) 555-0147
    </div>
    <div class="contact__line contact__mail">
      <svg width="12" height="9" viewBox="0 0 24 18" aria-hidden="true"><rect x="1" y="1" width="22" height="16" fill="none" stroke="#fff" stroke-width="2"/><path d="M1 1l11 9 11-9" fill="none" stroke="#fff" stroke-width="2"/></svg>
      info@brightkeyrentals-example.com
    </div>
    <div class="contact__line contact__addr">
      <svg width="9" height="12" viewBox="0 0 18 24" aria-hidden="true"><path d="M9 0a9 9 0 0 0-9 9c0 6.5 9 15 9 15s9-8.5 9-15a9 9 0 0 0-9-9zm0 12.5A3.5 3.5 0 1 1 9 5.5a3.5 3.5 0 0 1 0 7z" fill="#fff"/></svg>
      2287 Marble Lane, Lubbock, TX 79555
    </div>
  </div>
</section>

<!-- BACK -->
<section class="card card--back" aria-label="Postcard back">
  <svg class="band" width="655" height="473" aria-hidden="true">
    <polygon points="0,0 655,0 655,13 340,13 393,73 0,73" fill="var(--navy)"/>
  </svg>
  <h2 class="services-title"><span class="muted">OUR</span> SERVICES</h2>
  <p class="services-sub">WE OFFER FULL-SERVICE PROPERTY MANAGEMENT SOLUTIONS</p>

  <div class="brand">BrightKey<br>Rentals</div>

  <!-- left column -->
  <div class="service" style="left:24px;top:79px">
    <svg class="service__mark" viewBox="0 0 14 10" aria-hidden="true"><polygon points="6,0 10,0 4,10 0,10" fill="var(--grey)"/><polygon points="11,0 14,0 8,10 5,10" fill="var(--navy)"/></svg>
    <h3 class="service__title">PROPERTY MARKETING</h3>
    <svg class="service__icon" viewBox="0 0 40 40" aria-hidden="true"><polygon points="3,18 18,4 33,18 33,38 3,38" fill="var(--grey)"/><circle cx="30" cy="17" r="8" fill="#fff" stroke="var(--grey)" stroke-width="2"/><text x="30" y="21" font-size="11" text-anchor="middle" fill="var(--grey)" font-family="Montserrat,sans-serif">$</text></svg>
    <p class="service__body">Tired of waiting for weeks<br>on end, hoping to find a<br>new tenant? Let us take<br>over your marketing for<br>you and we'll find<br>a qualified renter quickly.</p>
  </div>
  <div class="service" style="left:24px;top:160px">
    <svg class="service__mark" viewBox="0 0 14 10" aria-hidden="true"><polygon points="6,0 10,0 4,10 0,10" fill="var(--grey)"/><polygon points="11,0 14,0 8,10 5,10" fill="var(--navy)"/></svg>
    <h3 class="service__title">RENT COLLECTION</h3>
    <svg class="service__icon" viewBox="0 0 40 40" aria-hidden="true"><circle cx="20" cy="10" r="7" fill="var(--grey)"/><text x="20" y="14" font-size="10" text-anchor="middle" fill="#fff" font-family="Montserrat,sans-serif">$</text><polygon points="6,26 20,16 34,26 34,38 6,38" fill="var(--grey)"/><rect x="16" y="27" width="8" height="6" fill="#fff"/><line x1="0" y1="38" x2="40" y2="38" stroke="var(--grey)" stroke-width="2"/></svg>
    <p class="service__body">Stop guessing when<br>you'll receive your rental<br>earnings every month<br>and say hello to consistent<br>payments. We keep<br>your tenants current.</p>
  </div>
  <div class="service" style="left:24px;top:241px">
    <svg class="service__mark" viewBox="0 0 14 10" aria-hidden="true"><polygon points="6,0 10,0 4,10 0,10" fill="var(--grey)"/><polygon points="11,0 14,0 8,10 5,10" fill="var(--navy)"/></svg>
    <h3 class="service__title">PROPERTY INSPECTIONS</h3>
    <svg class="service__icon" viewBox="0 0 40 40" aria-hidden="true"><circle cx="16" cy="16" r="13" fill="var(--grey)"/><polygon points="8,17 16,10 24,17 24,23 8,23" fill="#fff"/><line x1="26" y1="26" x2="37" y2="37" stroke="var(--grey)" stroke-width="4" stroke-linecap="round"/></svg>
    <p class="service__body">Inspections form<br>an important part of<br>our proactive property<br>management approach.<br>We visit every home in<br>our portfolio regularly.</p>
  </div>
  <div class="service" style="left:24px;top:320px">
    <svg class="service__mark" viewBox="0 0 14 10" aria-hidden="true"><polygon points="6,0 10,0 4,10 0,10" fill="var(--grey)"/><polygon points="11,0 14,0 8,10 5,10" fill="var(--navy)"/></svg>
    <h3 class="service__title">EVICTIONS</h3>
    <svg class="service__icon" viewBox="0 0 40 40" aria-hidden="true"><polygon points="3,14 18,3 33,14 33,32 3,32" fill="var(--grey)"/><circle cx="18" cy="15" r="4" fill="#fff"/><line x1="8" y1="22" x2="28" y2="30" stroke="#fff" stroke-width="2"/><line x1="28" y1="22" x2="8" y2="30" stroke="#fff" stroke-width="2"/><line x1="18" y1="32" x2="18" y2="40" stroke="var(--grey)" stroke-width="2"/></svg>
    <p class="service__body">When things go wrong<br>inside your rental home,<br>rest easy with the experts<br>on your side. We will<br>handle evictions for you &amp;<br>find new renters when its over.</p>
  </div>

  <!-- right column -->
  <div class="service" style="left:196px;top:79px">
    <svg class="service__mark" viewBox="0 0 14 10" aria-hidden="true"><polygon points="6,0 10,0 4,10 0,10" fill="var(--grey)"/><polygon points="11,0 14,0 8,10 5,10" fill="var(--navy)"/></svg>
    <h3 class="service__title">TENANT SCREENING</h3>
    <svg class="service__icon" viewBox="0 0 40 40" aria-hidden="true"><polygon points="2,18 11,11 20,18 20,28 2,28" fill="none" stroke="var(--grey)" stroke-width="2"/><circle cx="8" cy="34" r="4" fill="none" stroke="var(--grey)" stroke-width="2"/><line x1="12" y1="34" x2="36" y2="34" stroke="var(--grey)" stroke-width="2"/><circle cx="30" cy="12" r="6" fill="var(--grey)"/><path d="M22 30c0-6 4-10 8-10s8 4 8 10z" fill="var(--grey)"/></svg>
    <p class="service__body">We don't just find<br>someone to rent your<br>home—we find the best<br>renters. We screen all<br>applications using fair housing<br>guidelines to protect you.</p>
  </div>
  <div class="service" style="left:196px;top:160px">
    <svg class="service__mark" viewBox="0 0 14 10" aria-hidden="true"><polygon points="6,0 10,0 4,10 0,10" fill="var(--grey)"/><polygon points="11,0 14,0 8,10 5,10" fill="var(--navy)"/></svg>
    <h3 class="service__title">MAINTENANCE</h3>
    <svg class="service__icon" viewBox="0 0 40 40" aria-hidden="true"><polygon points="2,16 20,2 38,16 34,16 34,38 6,38 6,16" fill="var(--grey)"/><line x1="12" y1="32" x2="28" y2="18" stroke="#fff" stroke-width="3" stroke-linecap="round"/><line x1="12" y1="20" x2="28" y2="32" stroke="#fff" stroke-width="3" stroke-linecap="round"/></svg>
    <p class="service__body">Still scrambling to<br>respond to repair<br>requests every time<br>you receive a tenant<br>call? Let us coordinate<br>repair work on your behalf!</p>
  </div>
  <div class="service" style="left:196px;top:241px">
    <svg class="service__mark" viewBox="0 0 14 10" aria-hidden="true"><polygon points="6,0 10,0 4,10 0,10" fill="var(--grey)"/><polygon points="11,0 14,0 8,10 5,10" fill="var(--navy)"/></svg>
    <h3 class="service__title">FINANCIAL REPORTING</h3>
    <svg class="service__icon" viewBox="0 0 40 40" aria-hidden="true"><polygon points="8,2 28,2 34,8 34,38 8,38" fill="var(--grey)"/><text x="14" y="16" font-size="12" fill="#fff" font-family="Montserrat,sans-serif">$</text><rect x="13" y="26" width="3" height="8" fill="#fff"/><rect x="19" y="22" width="3" height="12" fill="#fff"/><rect x="25" y="18" width="3" height="16" fill="#fff"/></svg>
    <p class="service__body">Keep a handle on<br>your real estate performance.<br>We generate monthly<br>statements so you can<br>review income &amp; expenses<br>at a moment's notice.</p>
  </div>
  <div class="service" style="left:196px;top:320px">
    <svg class="service__mark" viewBox="0 0 14 10" aria-hidden="true"><polygon points="6,0 10,0 4,10 0,10" fill="var(--grey)"/><polygon points="11,0 14,0 8,10 5,10" fill="var(--navy)"/></svg>
    <h3 class="service__title">LEGAL GUIDANCE</h3>
    <svg class="service__icon" viewBox="0 0 40 40" aria-hidden="true"><line x1="12" y1="6" x2="12" y2="28" stroke="var(--grey)" stroke-width="3"/><line x1="2" y1="9" x2="22" y2="9" stroke="var(--grey)" stroke-width="2"/><path d="M0 18h8l-4-8zM16 18h8l-4-8z" fill="var(--grey)"/><rect x="6" y="28" width="12" height="3" fill="var(--grey)"/><circle cx="31" cy="22" r="5" fill="var(--grey)"/><path d="M22 40c0-8 4-12 9-12s9 4 9 12z" fill="var(--grey)"/></svg>
    <p class="service__body">Don't accidentally<br>violate one of the many<br>ordinances and housing<br>laws governing your<br>relationship with your tenants.<br>Let us keep you compliant.</p>
  </div>

  <div class="divider"></div>
  <div class="divider-end"></div>

  <div class="stamp" aria-label="Stamp area"></div>
  <div class="address-line" style="top:283px"></div>
  <div class="address-line" style="top:314px"></div>
  <div class="address-line" style="top:344px"></div>

  <svg class="band" width="655" height="473" aria-hidden="true">
    <polygon points="264,401 655,401 655,473 0,473 0,461 316,461" fill="var(--navy)"/>
    <polygon points="23,419 269,419 304,456 23,456" fill="var(--grey-light)"/>
  </svg>
  <div class="cta"><span class="cta__text">Contact Our Team</span></div>
  <div class="contact">
    <div class="contact__line contact__phone">
      <svg width="13" height="13" viewBox="0 0 24 24" aria-hidden="true"><path d="M6.6 10.8a15 15 0 0 0 6.6 6.6l2.2-2.2c.3-.3.7-.4 1-.2 1.1.4 2.3.6 3.6.6.6 0 1 .4 1 1V20c0 .6-.4 1-1 1A17 17 0 0 1 3 4c0-.6.4-1 1-1h3.5c.6 0 1 .4 1 1 0 1.3.2 2.5.6 3.6.1.3 0 .7-.2 1z" fill="none" stroke="#fff" stroke-width="2"/></svg>
      (806) 555-0147
    </div>
    <div class="contact__line contact__mail">
      <svg width="12" height="9" viewBox="0 0 24 18" aria-hidden="true"><rect x="1" y="1" width="22" height="16" fill="none" stroke="#fff" stroke-width="2"/><path d="M1 1l11 9 11-9" fill="none" stroke="#fff" stroke-width="2"/></svg>
      info@brightkeyrentals-example.com
    </div>
    <div class="contact__line contact__addr">
      <svg width="9" height="12" viewBox="0 0 18 24" aria-hidden="true"><path d="M9 0a9 9 0 0 0-9 9c0 6.5 9 15 9 15s9-8.5 9-15a9 9 0 0 0-9-9zm0 12.5A3.5 3.5 0 1 1 9 5.5a3.5 3.5 0 0 1 0 7z" fill="#fff"/></svg>
      2287 Marble Lane, Lubbock, TX 79555
    </div>
  </div>
</section>

</body>
</html>
```